Stationary for 2-office law firm with global theme

I need stationary with contact info for two offices. I'd like the same letterhead design to work for printing on stationary and also for digital use in Word. The colors and feel should match the new logo, which is a stylized globe with and "F" in it. I'd also like envelopes with an eye-catching design.

Target Market(s)

U.S. citizens seeking dual citizenship with Italy or Ireland

Industry/Entity Type

Law

Font styles to use
Serif
Sans Serif
Other font styles liked:
• To match the logo?

Colors
0054AA
0677BA
7BADD7
CADEEF
E8F1F8

Requirements
Must have
• Clean, modern design incorporating new logo

```html
<!DOCTYPE html>
<html lang="en">
<head>
<meta charset="utf-8">
<title>Castellan Law Stationery</title>
<link href="https://fonts.googleapis.com/css2?family=Arimo:wght@400;700&display=swap" rel="stylesheet">
<style>
  :root {
    --navy: #0054AA;
    --blue: #0677BA;
    --cyan: #00B7E8;
    --sky: #7BADD7;
    --mist: #CADEEF;
    --ice: #E8F1F8;
    --ink: #1f2328;
    --paper: #f5f5ef;
    --envelope: #ffffff;
    --backdrop: #e7e4de;
  }
  * { box-sizing: border-box; margin: 0; padding: 0; }
  html, body { width: 1200px; height: 850px; overflow: hidden; }
  body {
    background: var(--backdrop);
    font-family: "Arimo", Arial, sans-serif;
    color: var(--ink);
    position: relative;
  }

  .letterhead {
    position: absolute;
    left: 90px; top: 122px;
    width: 470px; height: 606px;
    background: var(--paper);
    box-shadow: 0 6px 18px rgba(0,0,0,.18);
    overflow: hidden;
  }
  .brand { display: flex; align-items: center; gap: 10px; }
  .brand-dot {
    width: 30px; height: 30px; border-radius: 50%;
    background: var(--blue);
    flex: none;
  }
  .brand-name {
    font-weight: 700;
    color: var(--navy);
    letter-spacing: .02em;
    line-height: 1;
  }
  .letterhead .brand { position: absolute; left: 37px; top: 42px; }
  .letterhead .brand-name { font-size: 21px; }

  .corner-art { position: absolute; }
  .letterhead .corner-top {
    right: 0; top: 0;
    width: 122px; height: 120px;
    border-bottom-left-radius: 100% 100%;
    background: linear-gradient(160deg, var(--cyan) 0%, var(--blue) 55%, var(--navy) 100%);
  }
  .letterhead .corner-bottom {
    right: 0; bottom: 0;
    width: 228px; height: 225px;
    border-top-left-radius: 100% 100%;
    background: linear-gradient(160deg, var(--ice) 0%, var(--mist) 100%);
    opacity: .75;
  }

  .letterhead-footer {
    position: absolute; left: 36px; bottom: 30px;
    font-size: 7.5px; line-height: 1.3;
    display: flex; gap: 34px; align-items: flex-end;
  }
  .address { margin-bottom: 10px; }
  .contact-list { list-style: none; }
  .contact-list li { display: flex; align-items: center; gap: 5px; line-height: 1.35; }
  .contact-icon { width: 7px; height: 7px; flex: none; }

  .envelope {
    position: absolute;
    left: 610px; top: 306px;
    width: 515px; height: 237px;
    background: var(--envelope);
    box-shadow: 0 6px 18px rgba(0,0,0,.18);
    overflow: hidden;
  }
  .envelope .brand {
    position: absolute; left: 28px; top: 30px;
    flex-direction: column; align-items: flex-start; gap: 8px;
  }
  .envelope .brand-dot { width: 34px; height: 34px; margin-left: 26px; }
  .envelope .brand-name { font-size: 16px; }
  .envelope .address {
    position: absolute; left: 29px; top: 108px;
    font-size: 8.5px; line-height: 1.35;
  }
  .envelope .corner-art {
    right: 0; bottom: 0;
    width: 116px; height: 112px;
    border-top-left-radius: 100% 100%;
    background: linear-gradient(165deg, var(--cyan) 0%, var(--cyan) 55%, var(--navy) 100%);
  }
</style>
</head>
<body>

<section class="letterhead">
  <div class="corner-art corner-top" role="img" aria-label="Brand globe graphic in blue tones"></div>
  <div class="corner-art corner-bottom" role="img" aria-label="Faint brand globe watermark"></div>

  <div class="brand">
    <span class="brand-dot"></span>
    <span class="brand-name">CASTELLAN LAW</span>
  </div>

  <footer class="letterhead-footer">
    <div class="office">
      <p class="address">214 Alder Court<br>Fairbanks, Alaska 99701</p>
      <ul class="contact-list">
        <li>
          <svg class="contact-icon" viewBox="0 0 10 10" aria-hidden="true">
            <circle cx="5" cy="5" r="5" fill="var(--blue)"/>
            <path d="M3.2 2.6c.3-.3.7-.3.9 0l.5.7c.2.3.1.6-.1.8l-.3.2c.3.6.8 1.1 1.4 1.4l.2-.3c.2-.2.5-.3.8-.1l.7.5c.3.2.3.6 0 .9l-.4.4c-1.6.3-4.2-2.3-3.9-3.9z" fill="#fff"/>
          </svg>
          555-218-4096
        </li>
        <li>
          <svg class="contact-icon" viewBox="0 0 10 10" aria-hidden="true">
            <circle cx="5" cy="5" r="5" fill="var(--blue)"/>
            <rect x="2.4" y="3.2" width="5.2" height="3.6" fill="#fff"/>
            <path d="M2.4 3.2L5 5.3l2.6-2.1" fill="none" stroke="var(--blue)" stroke-width=".6"/>
          </svg>
          info@castellanlaw.com
        </li>
        <li>
          <svg class="contact-icon" viewBox="0 0 10 10" aria-hidden="true">
            <circle cx="5" cy="5" r="5" fill="var(--blue)"/>
            <path d="M3 5h4M5 3v4" stroke="#fff" stroke-width=".8"/>
          </svg>
          www.castellanlaw.com
        </li>
      </ul>
    </div>
    <div class="office">
      <p class="address">88 Harbor Street<br>Juneau, Alaska 99801</p>
      <ul class="contact-list">
        <li>
          <svg class="contact-icon" viewBox="0 0 10 10" aria-hidden="true">
            <circle cx="5" cy="5" r="5" fill="var(--blue)"/>
            <path d="M3.2 2.6c.3-.3.7-.3.9 0l.5.7c.2.3.1.6-.1.8l-.3.2c.3.6.8 1.1 1.4 1.4l.2-.3c.2-.2.5-.3.8-.1l.7.5c.3.2.3.6 0 .9l-.4.4c-1.6.3-4.2-2.3-3.9-3.9z" fill="#fff"/>
          </svg>
          555-304-7718
        </li>
      </ul>
    </div>
  </footer>
</section>

<section class="envelope">
  <div class="brand">
    <span class="brand-dot"></span>
    <span class="brand-name">CASTELLAN LAW</span>
  </div>
  <p class="address">214 Alder Court<br>Fairbanks, Alaska 99701</p>
  <div class="corner-art" role="img" aria-label="Brand globe graphic in cyan and navy"></div>
</section>

</body>
</html>
```